Web page for Marcus Penrose Chartered Tax Adviser

I need to take the basic web page that I have created and "Brand it" to be compatible with the corporate logo and stationery created for me by other Pixel Guild designers.
I will need a watermark as well as a distinctive home page and then a branded general page for content including a series of Blogs.

Target Market(s)

My practice deals with expatriates including those looking to invest in Australia.

Industry/Entity Type

Crowd

Font styles to use
Other font styles liked:
• Per logo

Requirements
Must have
• Besides the homepage I will need a general page for content, branded in the same style as the letterheads.
Nice to have
• A watermark to go with the blogs and news content.

```html
<!DOCTYPE html>
<html lang="en">
<head>
<meta charset="utf-8">
<title>Marcus Penrose Chartered Tax Adviser</title>
<link rel="stylesheet" href="https://fonts.googleapis.com/css2?family=Cinzel:wght@500;600&family=Open+Sans:wght@400;700&display=swap">
<style>
:root{
  --navy:#2a4068;
  --navy-dark:#1f3153;
  --teal:#2f6a8c;
  --text:#555b63;
  --dark:#1e1e1e;
  --grey:#b9bcc2;
  --white:#ffffff;
}
*{margin:0;padding:0;box-sizing:border-box}
html,body{width:931px;height:1200px;overflow:hidden;background:var(--white)}
body{position:relative;font-family:"Open Sans",sans-serif;color:var(--text)}
.layer{position:absolute;left:0;top:0}
.brand{position:absolute;left:58px;top:22px;display:flex;align-items:center;gap:7px;color:var(--navy);font-family:"Cinzel",serif;font-weight:600}
.brand-mark{width:30px;height:30px;background:var(--navy)}
.brand-name{font-size:15px;line-height:1}
.brand-tag{font-size:7px;letter-spacing:2.4px;margin-top:3px}
.nav{position:absolute;top:28px;right:57px;display:flex;gap:32px;list-style:none}
.nav a{font-size:10px;color:var(--dark);text-decoration:none;letter-spacing:.3px}
.hero-caption{position:absolute;left:0;top:451px;width:585px;height:86px;background:var(--navy);color:var(--white);font-size:19.5px;line-height:29px;padding:12px 0 0 57px}
.section-title{font-family:"Cinzel",serif;font-weight:600;color:var(--navy);letter-spacing:.5px}
.services-title{position:absolute;left:57px;top:568px;font-size:17px}
.services{position:absolute;top:603px;list-style:none}
.services.left{left:57px}
.services.right{left:477px}
.services li{font-size:11px;line-height:20px;display:flex;align-items:center;gap:6px;white-space:nowrap}
.services svg{flex:none}
.experience{position:absolute;left:57px;top:755px;width:816px;height:121px;background:linear-gradient(100deg,#f1f2f4 0%,#e7e8eb 45%,#c9ccd1 75%,#8d9097 100%);padding:20px 20px 0 19px}
.experience h2{font-size:22px;font-weight:700;color:var(--navy);line-height:26px}
.experience p{font-size:10.2px;line-height:17px;color:var(--dark);margin-top:2px}
.footer-col{position:absolute;top:1040px;color:var(--white)}
.footer-col h3{font-size:13.5px;margin-bottom:5px;color:var(--white)}
.footer-col p,.footer-col a{font-size:9.6px;line-height:19px;color:var(--white)}
.footer-col a{display:block;text-decoration:underline;line-height:20.5px}
.col-about{left:57px;width:350px}
.col-links{left:476px}
.col-contact{left:684px}
.bottom-bar{position:absolute;left:0;top:1170px;width:931px;height:30px;background:var(--navy-dark);color:var(--white)}
.copyright{position:absolute;left:57px;top:9px;font-size:8.6px;font-weight:700;letter-spacing:.2px}
.social{position:absolute;right:64px;top:8px;display:flex;gap:2px;list-style:none}
.social li{width:14px;height:14px;border-radius:50%;background:var(--white)}
</style>
</head>
<body>
<svg class="layer" width="931" height="1200" viewBox="0 0 931 1200">
  <defs>
    <linearGradient id="headerShade" x1="0" y1="0" x2="1" y2="0">
      <stop offset="0" stop-color="#ffffff"/>
      <stop offset="1" stop-color="#d9dadd"/>
    </linearGradient>
    <linearGradient id="heroTones" x1="0" y1="0" x2="0" y2="1">
      <stop offset="0" stop-color="#d9e3e9"/>
      <stop offset=".55" stop-color="#c4cfd6"/>
      <stop offset="1" stop-color="#9aa3ab"/>
    </linearGradient>
    <linearGradient id="swoosh" x1="0" y1="0" x2="1" y2="0">
      <stop offset="0" stop-color="#233a63"/>
      <stop offset="1" stop-color="#2f7196"/>
    </linearGradient>
  </defs>
  <path d="M380,0 H931 V90 C780,60 620,80 520,100 C470,60 420,20 380,0Z" fill="url(#headerShade)"/>
  <path role="img" aria-label="Photo of two businesswomen shaking hands across an office desk by a window" d="M0,140 C220,175 560,130 931,92 V498 H0Z" fill="url(#heroTones)"/>
  <path d="M0,140 C220,175 560,130 931,92 V60 C600,80 300,140 0,120Z" fill="#ffffff"/>
  <path d="M58,122 C200,160 400,150 545,97 C400,140 220,150 58,122Z" fill="url(#swoosh)" stroke="url(#swoosh)" stroke-width="3"/>
  <path d="M47,945 C250,985 600,895 883,952" fill="none" stroke="var(--grey)" stroke-width="4"/>
  <path d="M0,980 C160,1022 360,1012 560,972 C720,940 850,948 931,975 V1170 H0Z" fill="var(--navy)"/>
</svg>

<header>
  <div class="brand">
    <span class="brand-mark"></span>
    <div>
      <div class="brand-name">Marcus Penrose</div>
      <div class="brand-tag">CHARTERED TAX ADVISER</div>
    </div>
  </div>
  <ul class="nav">
    <li><a href="#">HOME</a></li>
    <li><a href="#">ABOUT</a></li>
    <li><a href="#">BLOG</a></li>
    <li><a href="#">CONTACT US</a></li>
  </ul>
</header>

<p class="hero-caption">Tax advisers use their knowledge of tax legislation to provide advisory and consultancy services to clients</p>

<h2 class="section-title services-title">OUR SERVICES</h2>
<ul class="services left">
  <li><svg width="12" height="10" viewBox="0 0 12 10"><path d="M1,5 L4.5,8.5 L11,1.5" fill="none" stroke="#2a4068" stroke-width="2.2"/></svg>Researching, analysing and interpreting changing tax legislation</li>
  <li><svg width="12" height="10" viewBox="0 0 12 10"><path d="M1,5 L4.5,8.5 L11,1.5" fill="none" stroke="#2a4068" stroke-width="2.2"/></svg>Meeting with clients and collating information</li>
  <li><svg width="12" height="10" viewBox="0 0 12 10"><path d="M1,5 L4.5,8.5 L11,1.5" fill="none" stroke="#2a4068" stroke-width="2.2"/></svg>Working with tax law and revenue provisions</li>
  <li><svg width="12" height="10" viewBox="0 0 12 10"><path d="M1,5 L4.5,8.5 L11,1.5" fill="none" stroke="#2a4068" stroke-width="2.2"/></svg>Preparing and submitting compliance (tax) returns by the deadline</li>
  <li><svg width="12" height="10" viewBox="0 0 12 10"><path d="M1,5 L4.5,8.5 L11,1.5" fill="none" stroke="#2a4068" stroke-width="2.2"/></svg>Liaising and negotiating with the National Revenue Office</li>
  <li><svg width="12" height="10" viewBox="0 0 12 10"><path d="M1,5 L4.5,8.5 L11,1.5" fill="none" stroke="#2a4068" stroke-width="2.2"/></svg>Providing consultancy services to high value private clients</li>
</ul>
<ul class="services right">
  <li><svg width="12" height="10" viewBox="0 0 12 10"><path d="M1,5 L4.5,8.5 L11,1.5" fill="none" stroke="#2a4068" stroke-width="2.2"/></svg>Creating tax strategies for clients and planning their financial futures</li>
  <li><svg width="12" height="10" viewBox="0 0 12 10"><path d="M1,5 L4.5,8.5 L11,1.5" fill="none" stroke="#2a4068" stroke-width="2.2"/></svg>Carrying out detailed computations to calculate tax liability</li>
  <li><svg width="12" height="10" viewBox="0 0 12 10"><path d="M1,5 L4.5,8.5 L11,1.5" fill="none" stroke="#2a4068" stroke-width="2.2"/></svg>Advising on how to minimise a client's liability</li>
  <li><svg width="12" height="10" viewBox="0 0 12 10"><path d="M1,5 L4.5,8.5 L11,1.5" fill="none" stroke="#2a4068" stroke-width="2.2"/></svg>Establishing and structuring family trusts</li>
  <li><svg width="12" height="10" viewBox="0 0 12 10"><path d="M1,5 L4.5,8.5 L11,1.5" fill="none" stroke="#2a4068" stroke-width="2.2"/></svg>Estate planning and advising on tax residence and domicile matters</li>
  <li><svg width="12" height="10" viewBox="0 0 12 10"><path d="M1,5 L4.5,8.5 L11,1.5" fill="none" stroke="#2a4068" stroke-width="2.2"/></svg>Providing guidance on indirect taxation issues such as VAT</li>
</ul>

<section class="experience" role="img" aria-label="Soft grey background of tax forms and a pen behind the text">
  <h2>With over 16 years</h2>
  <p>Tax advisers can work in compliance, ensuring a client meets all tax obligations by preparing and submitting tax returns, tax computations and any other necessary forms. Alternatively, they may work in consultancy, advising clients on how to minimise their tax liabilities. Some self-employed tax advisers also offer their clients a range of accountancy services, such as bookkeeping, payroll and VAT.</p>
</section>

<footer>
  <div class="footer-col col-about">
    <h3 class="section-title">ABOUT MARCUS PENROSE SERVICES</h3>
    <p>Vivamus non elementum enim. Vestibulum fringilla placerat vestibulum. Donec consequat scelerisque lorem, quis laoreet tortor dapibus nec. Duis sodales quis odio quis pretium. Etiam auctor sollicitudin enim. Duis tempus semper sodales. Duis sodales quis odio quis pretium.</p>
  </div>
  <div class="footer-col col-links">
    <h3 class="section-title">USEFUL LINKS</h3>
    <a href="#">About Us</a>
    <a href="#">Services</a>
    <a href="#">Blog</a>
    <a href="#">Testimonials</a>
  </div>
  <div class="footer-col col-contact">
    <h3 class="section-title">CONTACT US</h3>
    <p>PO BOX 482150</p>
    <p>Eastbrook, FL 33071-4820</p>
    <p>(014) 5550 2817</p>
    <p>hello@marcuspenrose-tax.com</p>
  </div>
  <div class="bottom-bar">
    <p class="copyright">MARCUS PENROSE (C) COPYRIGHT 2014. ALL RIGHTS RESERVED</p>
    <ul class="social" aria-label="Social links">
      <li></li><li></li><li></li><li></li><li></li>
    </ul>
  </div>
</footer>
</body>
</html>
```